Packing for Razor Blade VORELIN

Dears: We need a packing design. The product is an Disposable Razor Blade. We are a company in Brazil.

The packing consists in a bag package which the Disposables Razos are placed. 5 units into each bag.

The bag is not 100% printed and should let a space to the customer see the razors inside. Some competitors uses oval circle. I attached competitor package (Tove Marigold)

The background color should be blue, this color tonality should vary its magnitude from dark blue to soft blue. Blue is a good color for personal care products because customer can take the impression of cleanness, especially for razor blade which has the fuction to shave.

You can feel free to add other colors however it can not be much colorfull because it may get trouble to printer company print it. Silver is good.

You can feel free to do details. You can feel free also to place the logo above the package or at bottom of it.

Dimmensions:
Heigh 24cm
Width 10cm

Featuring
- Featuring: Handle with Grip. In Portuguese - (Cabo Aderente)
- Featuring: 2 Razors. In portuguese - (Duas Lâminas)

Reason: I stayed many days with out providing feedbacks. I want to give more time for you .

Target Market(s)

Mans ( for woman we will design other package )

Requirements
Nice to have
• maybe some tears as a wet surface...
pls can feel free

```html
<!DOCTYPE html>
<html lang="pt-BR">
<head>
<meta charset="utf-8">
<title>VORELIN Super 5 – Embalagem</title>
<link href="https://fonts.googleapis.com/css2?family=Michroma&family=Roboto:ital,wght@0,900;1,900&display=swap" rel="stylesheet">
<style>
  :root {
    --blue-top: #2433e0;
    --blue-mid: #1722b8;
    --blue-deep: #0a0c6e;
    --navy: #050a45;
    --silver-light: #ffffff;
    --silver: #cfd3dc;
    --silver-dark: #8e95a6;
    --window: #ffffff;
    --text: #ffffff;
  }
  * { margin: 0; padding: 0; box-sizing: border-box; }
  html, body { width: 1200px; height: 2862px; overflow: hidden; }
  body { background: var(--navy); }
  .package {
    position: relative;
    width: 1200px;
    height: 2862px;
    overflow: hidden;
    background: linear-gradient(180deg, var(--blue-top) 0%, var(--blue-mid) 55%, var(--blue-deep) 85%, var(--navy) 100%);
    font-family: "Roboto", Arial, sans-serif;
  }
  .brand {
    position: absolute;
    top: 200px;
    left: 0;
    width: 100%;
    text-align: center;
    font-weight: 900;
    font-size: 180px;
    letter-spacing: 6px;
    color: var(--silver);
    line-height: 1;
  }
  .product-name {
    position: absolute;
    top: 660px;
    left: 0;
    width: 100%;
    text-align: center;
    font-family: "Michroma", "Arial Black", sans-serif;
    font-size: 118px;
    letter-spacing: 10px;
    line-height: 1;
    background: linear-gradient(180deg, var(--silver-light) 0%, var(--silver) 50%, var(--silver-dark) 100%);
    -webkit-background-clip: text;
    background-clip: text;
    color: transparent;
  }
  .artwork { position: absolute; inset: 0; }
  .window { fill: var(--window); }
  .gender-tag { fill: url(#tagGrad); }
  .gender-label {
    fill: var(--text);
    font-family: "Roboto", Arial, sans-serif;
    font-style: italic;
    font-weight: 900;
    font-size: 82px;
  }
  .count-badge-ring { fill: url(#badgeGrad); stroke: var(--silver); stroke-width: 10; }
  .count-number {
    fill: var(--text);
    stroke: var(--navy);
    stroke-width: 6;
    paint-order: stroke;
    font-family: "Roboto", Arial, sans-serif;
    font-style: italic;
    font-weight: 900;
    font-size: 190px;
  }
  .count-label {
    fill: var(--text);
    font-family: "Roboto", Arial, sans-serif;
    font-style: italic;
    font-weight: 900;
    font-size: 46px;
  }
  .features {
    position: absolute;
    left: 190px;
    top: 2410px;
    list-style: none;
    color: var(--text);
    font-style: italic;
    font-weight: 900;
    font-size: 86px;
    line-height: 84px;
  }
  .features li { position: relative; padding-left: 90px; margin-bottom: 32px; }
  .features .star {
    position: absolute;
    left: 10px;
    top: 22px;
    width: 40px;
    height: 40px;
    fill: var(--text);
  }
</style>
</head>
<body>
<main class="package">
  <div class="brand">VORELIN</div>
  <h1 class="product-name">SUPER 5</h1>

  <svg class="artwork" width="1200" height="2862" viewBox="0 0 1200 2862" aria-hidden="true">
    <defs>
      <linearGradient id="tagGrad" x1="0" y1="0" x2="1" y2="1">
        <stop offset="0" stop-color="#3a55ff"/>
        <stop offset="1" stop-color="#0d1690"/>
      </linearGradient>
      <radialGradient id="badgeGrad" cx="0.4" cy="0.35" r="0.7">
        <stop offset="0" stop-color="#1b2a9a"/>
        <stop offset="1" stop-color="#040836"/>
      </radialGradient>
      <clipPath id="windowClip">
        <path d="M138,902 C460,860 715,944 1112,890 C1060,1050 1000,1250 1030,1500 C1055,1750 1120,1900 1116,2300 C800,2270 500,2320 134,2300 C160,2050 230,1800 190,1580 C150,1380 138,1200 138,902 Z"/>
      </clipPath>
    </defs>

    <path class="window" d="M138,902 C460,860 715,944 1112,890 C1060,1050 1000,1250 1030,1500 C1055,1750 1120,1900 1116,2300 C800,2270 500,2320 134,2300 C160,2050 230,1800 190,1580 C150,1380 138,1200 138,902 Z"/>

    <g clip-path="url(#windowClip)">
      <polygon class="gender-tag" points="120,860 420,860 120,1150"/>
      <text class="gender-label" x="0" y="0" transform="translate(175,1075) rotate(-42)">man</text>
    </g>

    <g class="count-badge">
      <circle class="count-badge-ring" cx="923" cy="2140" r="158"/>
      <text class="count-number" x="923" y="2145" text-anchor="middle">5</text>
      <text class="count-label" x="923" y="2208" text-anchor="middle">Aparelhos</text>
    </g>
  </svg>

  <ul class="features">
    <li>
      <svg class="star" viewBox="0 0 24 24" aria-hidden="true"><path d="M12 1l3.1 7.2 7.9.7-6 5.2 1.8 7.7L12 17.8 5.2 21.8 7 14.1 1 8.9l7.9-.7z"/></svg>
      Duas Lâminas<br>Paralelas
    </li>
    <li>
      <svg class="star" viewBox="0 0 24 24" aria-hidden="true"><path d="M12 1l3.1 7.2 7.9.7-6 5.2 1.8 7.7L12 17.8 5.2 21.8 7 14.1 1 8.9l7.9-.7z"/></svg>
      Cabo Aderente
    </li>
  </ul>
</main>
</body>
</html>
```